Dozing Heron

Need a business card for our restaurant. Restaurant and Bar in the mountains of North Idaho. Rustic looking card

Contact Information for Business Card

rustic design, wood and metal looking, primarily neutral colors

Requirements
Must have
• Name, address, phone number, website, email address

```html
<!DOCTYPE html>
<html lang="en">
<head>
<meta charset="utf-8">
<title>The Dozing Heron – Business Card</title>
<link rel="stylesheet" href="https://fonts.googleapis.com/css2?family=Jost:wght@500&family=Arimo:wght@400&display=swap">
<style>
  :root {
    --stage: #3a3a3a;
    --ink: #000000;
    --paper: #ffffff;
  }
  html, body {
    margin: 0;
    width: 1200px;
    height: 1200px;
    overflow: hidden;
    background: var(--stage);
  }
  .canvas {
    position: relative;
    width: 1200px;
    height: 1200px;
  }
  .card {
    position: absolute;
    width: 688px;
    height: 393px;
    border-radius: 25px;
    overflow: hidden;
    background: var(--ink);
  }
  .card--front { left: 266px; top: 158px; }
  .card--back  { left: 262px; top: 653px; }

  .front-panel {
    position: absolute;
    left: 0; top: 0;
    width: 688px; height: 393px;
  }
  .brand-mark {
    position: absolute;
    display: flex;
    align-items: center;
    justify-content: center;
    border-radius: 50%;
    box-sizing: border-box;
    text-align: center;
  }
  .card--front .brand-mark {
    left: 52px; top: 60px;
    width: 268px; height: 268px;
    border: 5px solid var(--ink);
  }
  .card--back .brand-mark {
    left: 208px; top: 61px;
    width: 274px; height: 274px;
    border: 5px solid var(--paper);
  }
  .brand-name {
    font-family: "Jost", sans-serif;
    font-weight: 500;
    font-size: 26px;
    line-height: 1.15;
    letter-spacing: 2px;
    text-transform: uppercase;
  }
  .card--front .brand-name { color: var(--ink); }
  .card--back .brand-name { color: var(--paper); }

  .contact {
    position: absolute;
    left: 394px;
    top: 91px;
    color: var(--paper);
    font-family: "Arimo", sans-serif;
  }
  .contact__name {
    font-family: "Jost", sans-serif;
    font-weight: 500;
    font-size: 29px;
    letter-spacing: 0.5px;
    margin: 0;
    line-height: 1;
  }
  .contact__role {
    font-size: 14.5px;
    margin: 3px 0 0;
  }
  .contact__address {
    font-size: 16px;
    line-height: 21px;
    margin: 22px 0 0;
    font-style: normal;
  }
  .contact__list {
    list-style: none;
    margin: 12px 0 0;
    padding: 0;
  }
  .contact__item {
    position: relative;
    font-size: 16px;
    line-height: 20.5px;
    padding-left: 25px;
  }
  .contact__icon {
    position: absolute;
    left: 0;
    top: 4px;
    width: 13px;
    height: 13px;
  }
</style>
</head>
<body>
<main class="canvas">

  <section class="card card--front" aria-label="Business card front">
    <svg class="front-panel" viewBox="0 0 688 393" aria-hidden="true">
      <path d="M0 0 L265 0 Q440 196.5 265 393 L0 393 Z" fill="var(--paper)"/>
    </svg>

    <div class="brand-mark">
      <span class="brand-name">The Dozing<br>Heron</span>
    </div>

    <div class="contact">
      <h1 class="contact__name">PAUL MARSH</h1>
      <p class="contact__role">President</p>
      <address class="contact__address">
        4120 Cedar Hollow Road<br>
        Birchwood Flats, Canada 40718
      </address>
      <ul class="contact__list">
        <li class="contact__item">
          <svg class="contact__icon" viewBox="0 0 16 16" aria-hidden="true">
            <path d="M3.6 1.2l2.3 2.9-1.4 1.6c.9 2 2.6 3.8 4.7 4.8l1.6-1.4 2.9 2.3-1.5 2.6C7 13.6 2.5 9.1 1 3.1z" fill="var(--paper)"/>
          </svg>555-204-7186
        </li>
        <li class="contact__item">
          <svg class="contact__icon" viewBox="0 0 16 16" aria-hidden="true">
            <rect x="4" y="0.8" width="8" height="14.4" rx="1.4" fill="none" stroke="var(--paper)" stroke-width="1.4"/>
            <line x1="7" y1="12.6" x2="9" y2="12.6" stroke="var(--paper)" stroke-width="1.2"/>
          </svg>555-319-2047
        </li>
        <li class="contact__item">
          <svg class="contact__icon" viewBox="0 0 16 16" aria-hidden="true">
            <rect x="1" y="3.5" width="14" height="9.5" fill="none" stroke="var(--paper)" stroke-width="1.3"/>
            <path d="M1 3.5 L8 9 L15 3.5" fill="none" stroke="var(--paper)" stroke-width="1.3"/>
          </svg>info@thedozingheron.com
        </li>
        <li class="contact__item">
          <svg class="contact__icon" viewBox="0 0 16 16" aria-hidden="true">
            <circle cx="8" cy="8" r="6.8" fill="var(--paper)"/>
            <path d="M5 4.5c1.5.3 2 1.5 1.3 2.6-.8 1 .4 2 1.5 2.3.8.3.4 2-.3 3M10 3.4c-.6 1 .3 1.8 1.4 1.9" fill="none" stroke="var(--ink)" stroke-width="1.1"/>
          </svg>www.thedozingheron.com
        </li>
      </ul>
    </div>
  </section>

  <section class="card card--back" aria-label="Business card back">
    <div class="brand-mark">
      <span class="brand-name">The Dozing<br>Heron</span>
    </div>
  </section>

</main>
</body>
</html>
```